Wordpress Design Project for Bankruptcy Law Office in San Francisco

our current website: www.dorvanelilaw.example

we would like to re-design it for wordpress to make it faster and a bit more modern.

content should be similar to what we have there right now but also we do family law

please include logo for law office:

Law Office of Marta K. Dorvaneli

Thank you.
Updates

please see attached word document with logos that we like as an example.

we do tend to like color red.  darker red.

Please submit your design variations and logo as soon as possible.   We would like to go over them and make our decision

Reason: Please create couple of more variations of logo for your design, so we can make our decision what we like the most. Please see word doc for samples: Text: Law Office Of Marta K. Dorvaneli

Reason: final touches

Target Market(s)

bankruptcy and family law clients

Industry/Entity Type

Family Law

Requirements
Must have
• see examples of law sites
http://marketing.lexoriba.example/testimonials

- new logo: Law Office of Marta K. Dorvaneli
- client intake form
- blog
- contact us form

Nice to have
• - map
- red color
- on the front page a nice photo of SF or a happy family

```html
<!DOCTYPE html>
<html lang="en">
<head>
<meta charset="utf-8">
<title>Law Office of Marta K. Dorvaneli</title>
<link href="https://fonts.googleapis.com/css2?family=Open+Sans:wght@400;600;700&family=Tinos&family=Archivo+Black&display=swap" rel="stylesheet">
<style>
:root{
  --page:#ebebeb;
  --band:#f1f1f1;
  --panel:#ffffff;
  --ink:#222;
  --muted:#666;
  --faint:#999;
  --red:#c8171e;
  --blue:#1b7fd6;
  --sky:#2aa0ea;
  --green:#7dbb1f;
  --black:#0d0d0d;
  --line:#dcdcdc;
  --tab:#4f8fd6;
}
*{box-sizing:border-box;margin:0;padding:0}
html,body{width:700px;height:1200px;overflow:hidden}
body{position:relative;background:var(--page);font-family:"Open Sans",Arial,sans-serif;color:var(--muted);font-size:8px;line-height:1.5}
.abs{position:absolute}

/* header */
.brand{left:36px;top:6px;display:flex;align-items:flex-start;gap:10px}
.brand-mark{width:70px;height:62px;background:var(--red)}
.brand-name{font-family:"Tinos",serif;color:#1a1a1a;font-size:24px;line-height:1.1;padding-top:20px}
.brand-name span{display:block;font-size:15px;padding-left:62px;padding-top:4px}
.top-contact{left:486px;top:28px;width:178px;height:20px;background:var(--black);color:#fff;font-size:8px;font-weight:700;padding:4px 12px}
.call-label{left:402px;top:52px;font-family:"Archivo Black",sans-serif;color:var(--sky);font-size:18px;letter-spacing:.5px}
.call-number{left:384px;top:70px;font-family:"Archivo Black",sans-serif;color:#111;font-size:20px}

.social-tab{left:666px;width:34px;background:var(--tab);color:#fff;border-radius:6px 0 0 6px;font-weight:700;font-size:13px;writing-mode:vertical-rl;transform:rotate(180deg);display:flex;align-items:center;justify-content:center}
.tab-one{top:35px;height:82px}
.tab-two{top:122px;height:84px}

.main-nav{left:24px;top:97px;width:642px;height:26px;background:linear-gradient(#333,#0a0a0a);display:flex}
.main-nav a{color:#fff;text-decoration:none;font-size:8px;padding:8px 13px 0 8px;position:relative}
.main-nav a::after{content:"";position:absolute;right:3px;top:4px;width:6px;height:6px;background:#eee}

/* slider */
.slider{left:24px;top:140px;width:650px;height:135px;background:var(--panel);border:1px solid var(--line)}
.slide-title{left:30px;top:6px;font-family:"Archivo Black",sans-serif;font-size:31px;color:#1e1e1e;transform:scaleY(1.3);transform-origin:left top;white-space:nowrap}
.slide-number{left:54px;top:58px;font-family:"Archivo Black",sans-serif;font-size:40px;color:var(--blue);transform:scaleY(1.2);transform-origin:left top;white-space:nowrap}
.slide-art{right:0;top:0;width:214px;height:133px;background:linear-gradient(135deg,#ffffff 0%,#c79a6c 40%,#6b3a18 75%,#3a1c08 100%)}
.pager{left:296px;top:292px;display:flex;gap:4px;align-items:center}
.pager i{width:7px;height:7px;border-radius:50%;background:#c9c9c9;display:block}

/* intro band */
.band{left:0;top:318px;width:700px;height:214px;background:var(--band)}
.welcome{left:24px;top:333px;width:319px;height:196px;background:var(--panel);padding:0 2px}
.welcome h1{font-size:10px;font-weight:400;color:#333;text-transform:uppercase;line-height:1.25;padding-left:30px;position:relative;margin-bottom:10px}
.welcome h1 svg{position:absolute;left:2px;top:1px}
.welcome p{font-size:8px;line-height:13.4px;color:#777}
.video{left:358px;top:333px;width:278px;height:173px;background:var(--black)}
.video-title{color:#eee;font-size:8.5px;padding:3px 8px;white-space:nowrap;overflow:hidden}
.video-frame{position:absolute;left:0;top:18px;width:278px;height:154px;background:radial-gradient(ellipse at 40% 45%,#bff2ff 0%,#4fbfe6 45%,#0b4f7d 100%)}

/* service cards */
.card{top:565px;width:152px;height:170px;background:var(--panel);padding:13px 17px}
.card h2{font-size:7px;font-weight:700;letter-spacing:1px;color:#333;text-transform:uppercase;line-height:1.3;margin-bottom:2px}
.card p{font-size:8px;line-height:10.6px;color:#666;border:1px solid #e6e6e6;padding:0 2px}
.btn{position:absolute;left:17px;width:67px;height:21px;background:var(--green);color:#fff;font-size:6.5px;font-weight:700;text-align:center;line-height:21px;border-radius:2px}

/* testimonials */
.testimonials{left:24px;top:766px;width:652px}
.testimonials h3{font-size:7px;font-weight:700;letter-spacing:1px;color:#333;margin-bottom:7px}
.quote-title{background:var(--panel);font-size:8px;padding:1px 2px;margin-bottom:8px;border-bottom:1px solid var(--line)}
.quote{background:var(--panel);font-size:7.6px;line-height:14.5px;padding:0 2px 3px}

/* footer */
.footer{left:0;top:903px;width:700px;height:262px;background:var(--band)}
.disclaimer{left:24px;top:913px;width:152px;background:var(--panel);font-size:8px;line-height:13.2px;padding:0 2px 4px}
.tweets{left:190px;top:916px;width:152px}
.col-title{font-size:7px;font-weight:700;letter-spacing:1px;color:#333;margin-bottom:9px}
.tweet{font-size:8px;line-height:1.5;margin-bottom:8px}
.tweet a{color:var(--blue);text-decoration:none}
.tweet small{display:block;color:var(--faint);font-size:6.5px}
.follow{border:1px solid var(--line);background:var(--panel);color:var(--green);font-size:7px;padding:2px 3px;margin-top:6px}
.contact-form{left:358px;top:916px;width:270px}
.contact-form label{display:block;font-size:7.6px;color:#444;margin-top:4px}
.contact-form .field{width:148px;height:12px;border:1px solid #aaa;background:#fff;margin-top:2px}
.contact-form .area{width:265px;height:105px;border:1px solid #aaa;background:#fff;margin-top:2px}
.submit{display:inline-block;margin-top:5px;background:var(--green);color:#fff;font-size:6.5px;font-weight:700;padding:4px 8px;border-radius:2px}
.copyright{left:24px;top:1176px;font-size:7px;color:var(--faint)}
</style>
</head>
<body>

<header>
  <div class="abs brand">
    <div class="brand-mark"></div>
    <div class="brand-name">Marta K. Dorvaneli<span>Law Office</span></div>
  </div>
  <div class="abs top-contact">Contact Us</div>
  <div class="abs call-label">Call us at</div>
  <div class="abs call-number">415-555-0172</div>
</header>

<div class="abs social-tab tab-one">Facenet</div>
<div class="abs social-tab tab-two">Chirper</div>

<nav class="abs main-nav">
  <a>About</a><a>Areas of Practice</a><a>Resources</a><a>Blog</a><a>FAQ</a><a>Contact Us</a>
</nav>

<section class="abs slider">
  <div class="abs slide-title">Feel free to call us</div>
  <div class="abs slide-number">415-555-0172</div>
  <div class="abs slide-art" role="img" aria-label="Photo of a wooden judge's gavel"></div>
</section>
<div class="abs pager">
  <svg width="12" height="12" viewBox="0 0 12 12"><circle cx="6" cy="6" r="6" fill="#aaa"/><path d="M7 3 4 6l3 3" stroke="#fff" stroke-width="1.5" fill="none"/></svg>
  <i></i><i></i><i></i><i></i><i></i><i></i>
  <svg width="12" height="12" viewBox="0 0 12 12"><circle cx="6" cy="6" r="6" fill="#aaa"/><path d="M5 3l3 3-3 3" stroke="#fff" stroke-width="1.5" fill="none"/></svg>
</div>

<div class="abs band"></div>
<section class="abs welcome">
  <h1><svg width="20" height="14" viewBox="0 0 20 14"><path d="M1 2l6-1 6 2 6-2v11l-6 2-6-2-6 1z M7 1v11 M13 3v11" fill="none" stroke="var(--green)" stroke-width="1.4"/></svg>Welcome to BK Law 172 – Complete Bankruptcy Information</h1>
  <p>The Law Offices of Marta K. Dorvaneli is a consumer law office dedicated to consumer protection and zealously defending the rights of our clients. We offer the big firm quality legal representation with a small firm individualized attention to each client. Our office offers services in: all types of consumer bankruptcy filings, i.e. Chapter 7, Chapter 13, Chapter 11, negotiating a settlement of your debts, assisting you in the defense of collection litigation and defending you against foreclosure. Please review our site and see what we may be able to offer you. Feel free to call us at (415) 555-0172 or use our free case evaluation form. Speak to a Lawyer Unlike some other law firms, when you call the Law Office of Marta K. Dorvaneli you will speak to an actual attorney. Not a paralegal or assistant. And even after retaining our office you will still speak to an attorney unlike other firms where you cannot get a hold of your attorney after several attempts.</p>
</section>
<section class="abs video">
  <div class="video-title">Law Office of Marta K. Dorvaneli created by Pixelwright</div>
  <div class="video-frame" role="img" aria-label="Video still: firm intro clip on a light blue background"></div>
</section>

<article class="abs card" style="left:24px">
  <h2>Debt Relief</h2>
  <p>Lorem ipsum dolor sit amet, consectetur adipisicing elit, sed do eiusmod tempor incididunt ut labore et dolore magna aliqua. Ut enim ad minim veniam, quis nostrud exercitation ullamco laboris nisi ut aliquip ex ea commodo consequat.</p>
  <span class="btn" style="top:146px">READ MORE</span>
</article>
<article class="abs card" style="left:191px">
  <h2>Foreclosure Prevention</h2>
  <p>Lorem ipsum dolor sit amet, consectetur adipisicing elit, sed do eiusmod tempor incididunt ut labore et dolore magna aliqua. Ut enim ad minim veniam.</p>
  <span class="btn" style="top:125px">READ MORE</span>
</article>
<article class="abs card" style="left:358px">
  <h2>Chapter 13</h2>
  <p>An individual with a regular income who is overcome by debts, but believes such debt can be repaid within a reasonable period of time, may file under chapter 13 of the bankruptcy code.</p>
  <span class="btn" style="top:115px">READ MORE</span>
</article>
<article class="abs card" style="left:525px">
  <h2>Chapter 7</h2>
  <p>Often called the liquidation chapter, or "fresh start," chapter 7 is used by individuals, families, partnerships, or corporations whose financial difficulties do not allow them to repay all of their debts.</p>
  <span class="btn" style="top:135px">READ MORE</span>
</article>

<section class="abs testimonials">
  <h3>TESTIMONIALS</h3>
  <div class="quote-title">Excellent Bankruptcy Attorney</div>
  <p class="quote">During our difficult financial times, we pretty much run out of all the possible options. Last option was bankruptcy and it was very difficult to decide on that and to understand what it is all about. It only took 30min with our consultation with Marta, that we really understood what all those chapters are about and understood our options. Before that chapter 7 or 13 were just numbers. Finally it was more clear what we can keep in bankruptcy solution and what we can't. Marta was very patient and made sure we have all of our questions answered before we went to next step. She also gave us materials to read at home. Once we decided to go for it, Ms. Dorvaneli sent us an online form, that was easy to fill out… from their she took care of everything. At court or any meetings we were explained every step. Once again Thank you very Much!!! Marta is very professional, experienced and understanding attorney.</p>
</section>

<div class="abs footer"></div>
<div class="abs disclaimer">Disclaimer: The Law Offices of Marta K. Dorvaneli is a Debt Relief law firm as defined by 11 U.S.C. 528. We help people file for Bankruptcy Relief under the Bankruptcy Code. The information contained on this website is not to be construed as legal advice. It is not intended to solicit or form an attorney-client relationship. We do not guarantee any result and prior results do not guarantee a similar outcome. This is an attorney advertisement and this website is for informational purposes only.</div>

<section class="abs tweets">
  <div class="col-title">LATEST TWEETS</div>
  <div class="tweet">Our Osaka team launched Beacon to help local users find critical information during moments of crisis <a>http://lnk.example/Qa72Rt</a><small>1 day ago</small></div>
  <div class="tweet">Check out our one-stop-shop for everything Starlights + Chirper! <a>http://lnk.example/Zp31Km</a><small>1 day ago</small></div>
  <div class="follow">Follow Me -&gt;</div>
</section>

<section class="abs contact-form">
  <div class="col-title">CONTACT US FORM</div>
  <label>Name:</label><div class="field"></div>
  <label>Email:</label><div class="field"></div>
  <label>Subject:</label><div class="field"></div>
  <label>Your Message:</label><div class="area"></div>
  <span class="submit">SUBMIT</span>
</section>

<div class="abs copyright">© Copyright 2012 Law Office of Marta K. Dorvaneli. All Rights Reserved.</div>

</body>
</html>
```